Packaging & Label Design for CDB Products

We are a European CBD company specialising in athletic recovery, sleep improvement and wellness.

We would like the packaging to incorporate our logo and name (and font 'Codec') 'Meridell CBD'. The design must be transferable to all of our products. CBD Oils, Balms, Lip Balm and Vape E-Liquid.

We would like it to be simple but eye-catching and modern. We don't want bright colours. Preferred pallet of muted greys, blacks, white and pastel colours. Geometric concepts, possibly using different colours for each item of the range, we are open to new and fresh ideas (we are seeking you for your experience) and when we find the right design we would likely throw more work in your direction..

Our product range is not complete so the designer must be flexible with some changes and provide files where format can be easily edited by packaging manufacturer. We are also waiting for dimensions for the labels and boxes for several products and will supply the designer with full dimensions of all products once selected.

Oil Box: 2.6 x 9.0 x 2.6 cm (open format 16.7 x 11.6cm)
Labels: 7.8 x 3.3 cm (Front and Back)

Our expected product range will be:
CBD Oil 1000mg
CBD Oil 3000mg
CBD Balm 100mg
CBD Balm 300mg
E-Liquid 500mg
Lip Balm 50mg

We look forward to seeing your ideas.

Best Regards
Meridell CBD

```html
<!DOCTYPE html>
<html lang="en">
<head>
<meta charset="utf-8">
<title>Meridell CBD – CBD Oil 1000 mg packaging</title>
<link rel="stylesheet" href="https://fonts.googleapis.com/css2?family=Montserrat:wght@500;700&family=Roboto+Condensed:wght@400;500&display=swap">
<style>
  :root {
    --backdrop: #e9e7e3;
    --paper-top: #ffffff;
    --paper-bottom: #e6e8e7;
    --mint: #b3dcc6;
    --mint-deep: #93b8a5;
    --ink: #1d1d1d;
    --shadow-ink: #2a2a2a;
  }
  * { margin: 0; padding: 0; box-sizing: border-box; }
  html, body {
    width: 1200px; height: 800px; overflow: hidden;
    background: var(--backdrop);
  }
  .canvas { position: relative; width: 1200px; height: 800px; }

  .panel {
    position: absolute;
    box-shadow: 0 10px 30px rgba(0,0,0,0.12);
  }
  .panel svg { position: absolute; inset: 0; display: block; }

  .box-front { left: 250px; top: 80px; width: 320px; height: 640px; }
  .bottle-label { left: 650px; top: 170px; width: 300px; height: 460px; border-radius: 4px; overflow: hidden; }

  .brand-name {
    position: absolute; left: 0; right: 0; text-align: center;
    font-family: "Montserrat", sans-serif; font-weight: 700;
    color: var(--ink); letter-spacing: 0.08em; text-transform: uppercase;
  }
  .box-front .brand-name { top: 190px; font-size: 26px; }
  .bottle-label .brand-name { top: 120px; font-size: 22px; }

  .product-title {
    position: absolute; text-align: right;
    font-family: "Roboto Condensed", sans-serif; font-weight: 500;
    color: var(--ink); line-height: 1;
  }
  .product-title .name { display: block; }
  .product-title .strength { display: block; font-weight: 400; }
  .box-front .product-title { right: 42px; top: 398px; }
  .box-front .product-title .name { font-size: 44px; }
  .box-front .product-title .strength { font-size: 22px; margin-top: 2px; }
  .bottle-label .product-title { right: 36px; top: 262px; }
  .bottle-label .product-title .name { font-size: 38px; }
  .bottle-label .product-title .strength { font-size: 19px; margin-top: 2px; }

  .volume {
    position: absolute; left: 0; right: 0; text-align: center;
    font-family: "Montserrat", sans-serif; font-weight: 500;
    color: var(--ink);
  }
  .box-front .volume { top: 590px; font-size: 15px; }
  .bottle-label .volume { top: 420px; font-size: 13px; }
</style>
</head>
<body>
<main class="canvas">

  <section class="panel box-front" aria-label="Oil box front panel">
    <svg viewBox="0 0 320 640" width="320" height="640" aria-hidden="true">
      <defs>
        <linearGradient id="boxPaper" x1="0" y1="0" x2="1" y2="0">
          <stop offset="0" stop-color="var(--paper-top)"/>
          <stop offset="1" stop-color="var(--paper-bottom)"/>
        </linearGradient>
        <linearGradient id="boxMint" x1="0" y1="0" x2="1" y2="1">
          <stop offset="0" stop-color="var(--mint)"/>
          <stop offset="1" stop-color="var(--mint-deep)"/>
        </linearGradient>
      </defs>
      <rect width="320" height="640" fill="url(#boxPaper)"/>
      <rect y="440" width="320" height="200" fill="url(#boxMint)"/>
      <path d="M66 470 C54 430 70 392 140 386 C210 380 296 376 300 420 C304 462 272 486 200 488 C140 490 78 504 66 470 Z"
            fill="var(--shadow-ink)"/>
      <path d="M74 462 C62 424 80 386 148 380 C216 374 302 372 304 414 C306 454 276 478 206 480 C146 482 86 496 74 462 Z"
            fill="var(--mint)"/>
    </svg>
    <p class="brand-name">Meridell CBD</p>
    <h2 class="product-title"><span class="name">CBD OIL</span><span class="strength">1000 mg</span></h2>
    <p class="volume">1 fl oz. ( 30ml )</p>
  </section>

  <section class="panel bottle-label" aria-label="Bottle front label">
    <svg viewBox="0 0 300 460" width="300" height="460" aria-hidden="true">
      <defs>
        <linearGradient id="labelPaper" x1="0" y1="0" x2="1" y2="0">
          <stop offset="0" stop-color="var(--paper-bottom)"/>
          <stop offset="0.5" stop-color="var(--paper-top)"/>
          <stop offset="1" stop-color="var(--paper-bottom)"/>
        </linearGradient>
        <linearGradient id="labelMint" x1="0" y1="0" x2="1" y2="1">
          <stop offset="0" stop-color="var(--mint)"/>
          <stop offset="1" stop-color="var(--mint-deep)"/>
        </linearGradient>
      </defs>
      <rect width="300" height="460" fill="url(#labelPaper)"/>
      <rect y="300" width="300" height="160" fill="url(#labelMint)"/>
      <path d="M52 330 C42 294 60 258 124 252 C190 246 276 244 280 286 C284 324 256 346 190 348 C132 350 64 364 52 330 Z"
            fill="var(--shadow-ink)"/>
      <path d="M60 322 C50 288 68 252 132 246 C196 240 282 240 284 280 C286 316 260 338 196 340 C140 342 72 356 60 322 Z"
            fill="var(--mint)"/>
    </svg>
    <p class="brand-name">Meridell CBD</p>
    <h2 class="product-title"><span class="name">CBD OIL</span><span class="strength">1000 mg</span></h2>
    <p class="volume">1 fl oz. ( 30ml )</p>
  </section>

</main>
</body>
</html>
```